Graphic Design Project

We make rose petal jelly from old fashioned english roses. The jelly is sweet eaten with scones and clotted cream or as a filling in a victoria sandwich, as a topping on ice cream or thick set yogurt.
The image of the product is luxurious and decadent and very english.
We need a design for a label which has a picture of an old fashioned rose (rosa mundi or a compte de chambard) The rose must stand out clearly so the jelly is not confused with other fruit jams. The overall colour of the label should be pink and soft, with white or dark pink writing. The label needs to be fridge proof.

We also need a security strip to fit on the lid of the jar.

We need the following information on the label.
Name of our company-"Meadow Lantern"
Name of Product-"Rose Petal Jelly"
Sales pitch-"With whole petals-a taste of summer, delicious on scones, as a filling in sponge cake, as a topping on ice cream or yogurt."
INGREDIENTS: Sugar, water, rose petals, lemon juice, natural jelling agent (agar-agar)
STORAGE: Store in a cool dry place, once opened keep refrigerated and consume within 4 weeks.
BEST BEFORE: See base

200g
Produced by:
MEADOW LANTERN
The Larches
Brindle Lane
Newnham
Gloucestershire
GL17 4QX
The label must have room for a bar code. The size of label approx 8-10cm long 5cm wide.
Updates

Hi

Just been looking at the Harrowgate and Pellow site and the labels they have there have the up market feel I am trying to convey. Hope that helps, its classy but not twee.

Thanks

Thanks for all submissions. I would be grateful if you googled images for 'Colourful and expensive biscuits at Harrowgate Pellow' The designs on the tins are the image we are trying to create. The colours are quite strong.

Thanks

Target Market(s)

older well off people who visit garden centres

Industry/Entity Type

Security

Requirements
Must have
• All writen info above and picture of old fashioned rose prferably rose a mundi. Luxury feel, very english, to appeal to older market
Pink colour sheme
Should not have
• dark or manly colours

```html
<!DOCTYPE html>
<html lang="en">
<head>
<meta charset="utf-8">
<title>Meadow Lantern Rose Petal Jelly Label</title>
<link rel="stylesheet" href="https://fonts.googleapis.com/css2?family=Crimson+Pro:wght@400&family=Arimo:wght@400&display=swap">
<style>
  :root {
    --paper: #ffffff;
    --ink: #111111;
    --rose-red: #e0222a;
    --panel-pink: #f7d7e9;
    --panel-glow: #ffffff;
    --petal-dark: #4f5552;
    --petal-light: #8d9390;
    --rule: #222222;
  }
  * { box-sizing: border-box; margin: 0; padding: 0; }
  html, body { width: 1200px; height: 750px; overflow: hidden; background: var(--paper); }
  .label {
    position: relative;
    width: 1200px;
    height: 750px;
    background: var(--paper);
    font-family: "Crimson Pro", "Times New Roman", serif;
    color: var(--ink);
  }
  .info-column {
    position: absolute;
    top: 26px;
    left: 22px;
    width: 270px;
    font-size: 23px;
    line-height: 24px;
  }
  .info-block { margin-bottom: 30px; }
  .info-block.storage { margin-bottom: 28px; }
  .front-panel {
    position: absolute;
    left: 295px;
    top: 0;
    width: 592px;
    height: 750px;
    background: radial-gradient(ellipse 62% 52% at 50% 50%, var(--panel-glow) 0%, var(--panel-pink) 100%);
    text-align: center;
  }
  .brand-name {
    position: absolute;
    top: 40px;
    left: 0;
    width: 100%;
    font-size: 54px;
    line-height: 60px;
    font-weight: 400;
  }
  .product-name {
    position: absolute;
    top: 120px;
    left: 0;
    width: 100%;
    font-size: 66px;
    line-height: 74px;
    font-weight: 400;
    color: var(--rose-red);
  }
  .tagline {
    position: absolute;
    top: 205px;
    left: 0;
    width: 100%;
    font-size: 25px;
    line-height: 30px;
  }
  .rose-art {
    position: absolute;
    left: 148px;
    top: 300px;
    width: 260px;
    height: 250px;
  }
  .serving-ideas {
    position: absolute;
    top: 586px;
    left: 0;
    width: 100%;
    font-size: 23px;
    line-height: 30px;
  }
  .net-weight {
    position: absolute;
    left: 498px;
    top: 712px;
    font-family: "Arimo", Arial, sans-serif;
    font-size: 25px;
  }
  .producer {
    position: absolute;
    top: 38px;
    left: 920px;
    font-size: 29px;
    line-height: 34.5px;
  }
  .barcode-space {
    position: absolute;
    left: 1000px;
    top: 636px;
    width: 177px;
    height: 90px;
    border: 1.5px solid var(--rule);
    padding: 22px 0 0 8px;
    font-family: "Arimo", Arial, sans-serif;
    font-size: 18px;
    line-height: 24px;
  }
</style>
</head>
<body>
<main class="label">
  <section class="info-column">
    <p class="info-block ingredients">INGREDIENTS:<br>Sugar, water, rose petals, lemon juice, natural jelling agent (agar-agar)</p>
    <p class="info-block storage">STORAGE: Store in a cool dry place, once opened keep refrigerated and consume within<br>4 weeks.</p>
    <p class="info-block best-before">BEST BEFORE:<br>See base</p>
  </section>

  <section class="front-panel">
    <h1 class="brand-name">Meadow Lantern</h1>
    <h2 class="product-name">Rose Petal Jelly</h2>
    <p class="tagline">"With whole petals its a taste of summer”</p>
    <svg class="rose-art" viewBox="0 0 260 250" role="img" aria-label="Three old fashioned roses in full bloom">
      <defs>
        <radialGradient id="bloom" cx="50%" cy="50%" r="50%">
          <stop offset="0%" stop-color="var(--petal-dark)"/>
          <stop offset="100%" stop-color="var(--petal-light)"/>
        </radialGradient>
      </defs>
      <circle cx="62" cy="72" r="58" fill="url(#bloom)"/>
      <circle cx="180" cy="62" r="60" fill="url(#bloom)"/>
      <circle cx="150" cy="178" r="62" fill="url(#bloom)"/>
    </svg>
    <p class="serving-ideas">Delicious on scones, as a filling<br>in sponge cake, as a topping<br>on ice cream or yogurt."</p>
    <p class="net-weight">200g</p>
  </section>

  <address class="producer" style="font-style:normal">
    Produced by:<br>MEADOW LANTERN<br>The Larches<br>Brindle Lane<br>Newnham<br>Gloucestershire<br>GL17 4QX
  </address>

  <div class="barcode-space">Bar<br>Code</div>
</main>
</body>
</html>
```